Best in Class Software Provider needs Powerpoint slides improved

We have an existing powerpoint that we have been using for companies we are selling into. In my opinion - the powerpoint needs work to make it look professional and pop more.

I'm looking for a powerpoint expert to take the existing slides and make them much more professional looking so we can email the deck to prospects we are selling into and partners.

Examples of the type of fixes we are looking for are (and are open to other fixes):

- change the font and make it consistent for all slides
- move the text, images, and boxes on the slides to make it cleaner, clearer, and better looking
- show you can magnify part of the images so it emphasizes specific areas of the picture (circle magnification to emphasize an area of the image)
- put an outline around the images or soften the edges so they look better
- change the color of the fonts to make it more professional and pop more - or size
- add icons to each slide to make it more professional - tech looking
- we selling into retailers, some small and some larger retailers so we need to be new wave looking but also professional looking
- look at the attached one pager on the product - to see colors and some design elements
- look at www.brightloop.com our website to make sure deck is consistent from a design standpoint as the website
- look at taskvane.com for inspiration on how their site looks clean

Ask questions if you have them?

We'll need the deck to be usable so I can change the text for other powerpoints in the future - so you can't send a PDF for example as I'll need a PPT.

We will continue to need powerpoint help over time and this could lead to more work.

The deck is attached.

Thanks,
Mark

Target Market(s)

We sell into retailers

Industry/Entity Type

Software

Requirements
Must have
• Make our ppt look amazing and professional -
Nice to have
• Our product design is at www.brightloop.com -
• We obsess over simplicity and easy to use and powerful software - that is a good guide for the design work on the powerpoint.

```html
<!DOCTYPE html>
<html lang="fr">
<head>
<meta charset="utf-8">
<title>Powerpoint Design Concept – BrightLoop</title>
<link href="https://fonts.googleapis.com/css2?family=Jost:wght@300;400;600;700&display=swap" rel="stylesheet">
<style>
:root{
  --teal:#1a9994;
  --teal-dark:#137c78;
  --charcoal:#3b3a3a;
  --white:#ffffff;
  --card-grey:#7b7b7b;
  --text-dark:#4a4a4a;
  --text-soft:#8a8a8a;
  --city-top:#8e8e8e;
  --city-mid:#bdbdbd;
  --city-low:#e9e9e9;
}
*{margin:0;padding:0;box-sizing:border-box}
html,body{width:848px;height:1200px;overflow:hidden}
body{font-family:"Jost",sans-serif;font-weight:300;background:var(--charcoal);position:relative}
.side-panel{position:absolute;left:0;top:0;width:226px;height:1200px;background:var(--teal)}
.board-title{position:absolute;left:30px;top:38px;color:var(--white);font-size:23px;line-height:29px;font-weight:300}
.brand-mark{position:absolute;left:712px;top:1142px;color:var(--white);font-weight:700;font-size:17px;letter-spacing:.2px}
.slide{position:absolute;left:326px;width:422px;height:317px;overflow:hidden}
.slide-bg{position:absolute;inset:0;background:linear-gradient(180deg,var(--city-top) 0%,var(--city-mid) 45%,var(--city-low) 70%,var(--city-mid) 100%)}
.slide-tab{position:absolute;left:176px;top:0;width:74px;height:37px}
.slide-footer{position:absolute;left:0;right:0;bottom:3px;text-align:center;color:var(--white);font-size:7px;font-weight:600}
.photo{position:absolute;background:linear-gradient(160deg,#cfcfcf,#6d6d6d)}
.tiny{font-size:4.3px;line-height:5.6px;color:var(--text-soft)}
/* slide 1 */
.s1{top:59px}
.profile-card{position:absolute;left:19px;top:53px;width:97px;height:230px;background:var(--card-grey)}
.profile-frame{position:absolute;left:0;top:0;width:97px;height:93px;background:var(--teal)}
.profile-card .photo{left:9px;top:8px;width:79px;height:80px}
.profile-name{position:absolute;left:0;right:0;top:104px;text-align:center;color:var(--white);font-size:9.5px}
.profile-role{position:absolute;left:0;right:0;top:118px;text-align:center;color:var(--white);font-size:7px}
.profile-card .tiny{position:absolute;left:10px;width:78px;color:#e6e6e6}
.partner-panel{position:absolute;left:116px;top:53px;width:298px;height:230px;background:var(--white)}
.partner{position:absolute;top:8px;width:76px}
.partner-logo{height:67px;border:1px solid var(--teal);display:flex;align-items:center;justify-content:center;gap:3px;color:var(--text-dark);font-size:9px;font-weight:400}
.partner-logo .dot{width:6px;height:6px;border-radius:50%;background:var(--teal)}
.partner h3{font-weight:400;font-size:7px;color:var(--text-dark);margin:12px 0 4px}
/* slide 2 */
.s2{top:428px}
.team-card{position:absolute;top:52px;width:97px}
.team-head{height:180px;background:var(--teal);position:relative}
.team-head .photo{left:8px;top:8px;width:81px;height:80px}
.team-name{position:absolute;left:0;right:0;top:96px;text-align:center;color:var(--white);font-size:9.5px}
.team-role{position:absolute;left:0;right:0;top:111px;text-align:center;color:var(--white);font-size:7px}
.team-text{background:var(--white);height:45px;margin-top:2px;padding:5px 7px}
/* slide 3 */
.s3{top:791px}
.steps-title{position:absolute;left:32px;top:32px;color:var(--teal);font-size:14px;font-weight:300}
.step-badge{position:absolute;left:63px;width:33px;height:33px;background:var(--teal);transform:rotate(45deg)}
.step-num{position:absolute;left:63px;width:33px;height:33px;line-height:33px;text-align:center;color:var(--white);font-size:12px}
.step-box{position:absolute;left:158px;width:230px;padding:7px 10px;font-size:4.4px;line-height:6px}
.step-box.filled{background:var(--teal);color:var(--white)}
.step-box.plain{background:var(--white);color:var(--teal)}
</style>
</head>
<body>
<aside class="side-panel"></aside>
<h1 class="board-title">Powerpoint<br>Design Concept</h1>

<!-- Slide: leadership and partners -->
<section class="slide s1">
  <div class="slide-bg" role="img" aria-label="Greyscale city skyline photograph"></div>
  <svg class="slide-tab" viewBox="0 0 74 37"><polygon points="0,0 74,0 37,37" fill="#1a9994"/><circle cx="37" cy="14" r="8" fill="none" stroke="#fff" stroke-width="1.6"/><polyline points="37,9 37,14 41,16" fill="none" stroke="#fff" stroke-width="1.6"/></svg>
  <div class="profile-card">
    <div class="profile-frame"><div class="photo" role="img" aria-label="Portrait photo of the CEO"></div></div>
    <div class="profile-name">Le Lorem Ipsum</div>
    <div class="profile-role">CEO</div>
    <p class="tiny" style="top:133px">Le Lorem Ipsum est simplement du faux texte employé dans la composition et la mise en page avant impression. Le Lorem Ipsum est le faux texte standard de l'imprimerie depuis les années.</p>
    <p class="tiny" style="top:178px">Le Lorem Ipsum est simplement du faux texte employé dans la composition et la mise en page avant impression. Le Lorem Ipsum est le faux texte standard de l'imprimerie depuis les années.</p>
  </div>
  <div class="partner-panel">
    <div class="partner" style="left:12px">
      <div class="partner-logo"><span class="dot"></span>Axle &amp; Co</div>
      <h3>Le Lorem Ipsum</h3>
      <p class="tiny">Le Lorem Ipsum est simplement du faux texte employé dans la composition et la mise en page avant impression. Le Lorem Ipsum est le faux texte standard de l'imprimerie depuis les années 1500, quand un peintre anonyme assembla ensemble des morceaux de texte pour réaliser un livre spécimen de polices de texte. Il n'a pas fait que survivre cinq siècles, mais s'est aussi adapté à la bureautique informatique, sans que son contenu n'en soit modifié. Il a été popularisé dans les années 1960 grâce à la vente de feuilles.</p>
    </div>
    <div class="partner" style="left:106px">
      <div class="partner-logo">Norvale</div>
      <h3 style="margin-top:17px">Le Lorem Ipsum</h3>
      <p class="tiny">Le Lorem Ipsum est simplement du faux texte employé dans la composition et la mise en page avant impression. Le Lorem Ipsum est le faux texte standard de l'imprimerie depuis les années 1500, quand un peintre anonyme assembla ensemble des morceaux de texte pour réaliser un livre spécimen de polices de texte. Il n'a pas fait que survivre cinq siècles, mais s'est aussi adapté à la bureautique informatique, sans que son contenu n'en soit modifié. Il a été popularisé dans les années 1960 grâce à la vente de feuilles.</p>
    </div>
    <div class="partner" style="left:200px">
      <div class="partner-logo"><span class="dot" style="border-radius:0"></span>Quadrant</div>
      <h3 style="margin-top:20px">Le Lorem Ipsum</h3>
      <p class="tiny">Le Lorem Ipsum est simplement du faux texte employé dans la composition et la mise en page avant impression. Le Lorem Ipsum est le faux texte standard de l'imprimerie depuis les années 1500, quand un peintre anonyme assembla ensemble des morceaux de texte pour réaliser un livre spécimen de polices de texte. Il n'a pas fait que survivre cinq siècles, mais s'est aussi adapté à la bureautique informatique, sans que son contenu n'en soit modifié. Il a été popularisé dans les années 1960 grâce à la vente de feuilles.</p>
    </div>
  </div>
  <div class="slide-footer">BrightLoop</div>
</section>

<!-- Slide: team -->
<section class="slide s2">
  <div class="slide-bg" role="img" aria-label="Greyscale city skyline photograph"></div>
  <svg class="slide-tab" viewBox="0 0 74 37"><polygon points="0,0 74,0 37,37" fill="#1a9994"/><circle cx="37" cy="14" r="8" fill="none" stroke="#fff" stroke-width="1.6"/><polyline points="37,9 37,14 41,16" fill="none" stroke="#fff" stroke-width="1.6"/></svg>
  <div class="team-card" style="left:51px">
    <div class="team-head"><div class="photo" role="img" aria-label="Portrait photo of the CEO"></div><div class="team-name">Le Lorem Ipsum</div><div class="team-role">CEO</div></div>
    <p class="team-text tiny">Le Lorem Ipsum est simplement du faux texte employé dans la composition et la mise en page avant impression. Le Lorem Ipsum est le faux texte standard de l'imprimerie depuis les années.</p>
  </div>
  <div class="team-card" style="left:164px">
    <div class="team-head"><div class="photo" role="img" aria-label="Portrait photo of the CFO" style="background:linear-gradient(160deg,#f2f2f2,#4a3a35)"></div><div class="team-name">Le Lorem Ipsum</div><div class="team-role">CFO</div></div>
    <p class="team-text tiny">Le Lorem Ipsum est simplement du faux texte employé dans la composition et la mise en page avant impression. Le Lorem Ipsum est le faux texte standard de l'imprimerie depuis les années.</p>
  </div>
  <div class="team-card" style="left:280px">
    <div class="team-head"><div class="photo" role="img" aria-label="Portrait photo of the CTO" style="background:linear-gradient(160deg,#2c3f5a,#7a5a48)"></div><div class="team-name">Le Lorem Ipsum</div><div class="team-role">CTO</div></div>
    <p class="team-text tiny">Le Lorem Ipsum est simplement du faux texte employé dans la composition et la mise en page avant impression. Le Lorem Ipsum est le faux texte standard de l'imprimerie depuis les années.</p>
  </div>
  <div class="slide-footer">BrightLoop</div>
</section>

<!-- Slide: steps -->
<section class="slide s3">
  <div class="slide-bg" role="img" aria-label="Greyscale city skyline photograph"></div>
  <svg class="slide-tab" viewBox="0 0 74 37"><polygon points="0,0 74,0 37,37" fill="#1a9994"/><circle cx="37" cy="14" r="8" fill="none" stroke="#fff" stroke-width="1.6"/><polyline points="37,9 37,14 41,16" fill="none" stroke="#fff" stroke-width="1.6"/></svg>
  <h2 class="steps-title">Le Lorem Ipsum</h2>
  <div class="step-badge" style="top:80px"></div><div class="step-num" style="top:80px">1</div>
  <div class="step-badge" style="top:158px"></div><div class="step-num" style="top:158px">2</div>
  <div class="step-badge" style="top:230px"></div><div class="step-num" style="top:230px">3</div>
  <p class="step-box filled" style="top:61px;height:70px">Le Lorem Ipsum est simplement du faux texte employé dans la composition et la mise en page avant impression. Le Lorem Ipsum est le faux texte standard de l'imprimerie depuis les années 1500, quand un peintre anonyme assembla ensemble des morceaux de texte pour réaliser un livre spécimen de polices de texte. Il n'a pas fait que survivre cinq siècles, mais s'est aussi adapté à la bureautique informatique, sans que son contenu n'en soit modifié. Il a été popularisé dans les années 1960 grâce à la vente de feuilles.</p>
  <p class="step-box plain" style="top:138px;height:68px">Le Lorem Ipsum est simplement du faux texte employé dans la composition et la mise en page avant impression. Le Lorem Ipsum est le faux texte standard de l'imprimerie depuis les années 1500, quand un peintre anonyme assembla ensemble des morceaux de texte pour réaliser un livre spécimen de polices de texte. Il n'a pas fait que survivre cinq siècles, mais s'est aussi adapté à la bureautique informatique, sans que son contenu n'en soit modifié. Il a été popularisé dans les années 1960 grâce à la vente de feuilles.</p>
  <p class="step-box filled" style="top:216px;height:70px">Le Lorem Ipsum est simplement du faux texte employé dans la composition et la mise en page avant impression. Le Lorem Ipsum est le faux texte standard de l'imprimerie depuis les années 1500, quand un peintre anonyme assembla ensemble des morceaux de texte pour réaliser un livre spécimen de polices de texte. Il n'a pas fait que survivre cinq siècles, mais s'est aussi adapté à la bureautique informatique, sans que son contenu n'en soit modifié. Il a été popularisé dans les années 1960 grâce à la vente de feuilles.</p>
  <div class="slide-footer">BrightLoop</div>
</section>

<div class="brand-mark">BrightLoop</div>
</body>
</html>
```